Jo & Mira's Homepage Design - Florists

Hello PixelHive,

We’re Jo and Mira and we own a lovely flower shop in Marlow. We’re looking to launch a website that gives our customers all information they need to know about getting in contact with us. In time we hope the website will grow and we will want to add new pages as we go along including ecommerce functionality, so the design will need to allow for this.

The brief:
We are looking for 1 homepage design. We have already had our logo designed, which we’ve attached for you to use. At the moment we’re keen to have a homepage design that showcases six of our most popular bouquets, see attached pictures and our contact details. We are looking for a contemporary design that’s inline with our logo. Please do not use dark background colours, we want a clean, light and simple design that looks fresh, modern and professional. Please remember that the majority of web monitors now use a screen resolution of 1366x768. Therefore please do not design a 800 x 600 homepage.

1. Our logo and icon (See attachments)
2. Potential hero images attached for inspiration. 6 Bouquets attached but dont make it look like a bog standard ecommerce site. You dont have to use the 6 bouquets. Our site is more brand as we dont have ecom functionality yet.
3. Our contact details including:

Name:
Jo and Mira’s (note 1 ‘L’ in Mira’s name, use the logo)

Navigation

Homepage needs to include the following copy
‘Free delivery with all orders”
‘Fresh – 7 days of flower freshness guaranteed’
‘Hand delivered and hand prepared by a professional florist’
Very clear call to action to ‘Order today: 0203 554 2071 or email us (visually a clickable link) today

Payment visuals: show that we accept PAYRO/Cardwell/Northern Swift/Quikpay, with logos

Telephone numbers:
0203 554 2071 (Central London)
0208 417 2359 (Greater London)
01628 570213 (Marlow)
07845 190627 (Mobile)

E-mail address
orders@joandmiras.co.uk (Orders)
CS@joandmiras.co.uk (Customer Service)

Chatterly page link (use CH logo)
http://www.facebook.com/joandmiras

The National Petal Guild logo
Attached should be displayed on the bottom of the homepage somewhere, prefer bottom right.

Other sites we like:
http://www.bloomsbyharriet.com
http://maisondepetale.com
Like the fun of this one - http://www.grandpagoose.co.uk/goto/home

Our logo should be a good guide for how we’d like the overall page to look, please use this as a starter for your designs. Fee; free to submit your designs and I’ll feedback on changes.

We look forward to seeing your designs!

Jo & Mira

Industry/Entity Type

Florist

Requirements
Must have
• Please see the attached brief. Please use our logo and icon in the design.
Should not have
• Do not use dark background colours, it should feel light and fresh.

```html
<!DOCTYPE html>
<html lang="en">
<head>
<meta charset="utf-8">
<title>Jo &amp; Mira's – Florists</title>
<link rel="stylesheet" href="https://fonts.googleapis.com/css2?family=Open+Sans:ital,wght@0,300;0,400;0,600;0,700;1,300&family=Oswald:wght@300;400&family=Exo+2:ital,wght@1,800&display=swap">
<style>
:root{
  --purple:#8a3e97;
  --purple-dark:#5e2068;
  --lilac:#b98ac3;
  --orange:#e0583a;
  --red:#d42a2a;
  --navy:#24313d;
  --text:#3a3a3a;
  --footer:#e9e9e9;
  --white:#ffffff;
}
*{box-sizing:border-box;margin:0;padding:0}
html,body{width:1000px;height:1200px;overflow:hidden}
body{position:relative;font-family:'Open Sans',sans-serif;color:var(--text);background:#fbeef2}
.abs{position:absolute}
.backdrop{position:absolute;inset:0;
  background:radial-gradient(circle at 8% 45%,#f3b6c8 0,#f7d3de 22%,transparent 40%),
             radial-gradient(circle at 92% 30%,#f1a8bf 0,#f6cad7 20%,transparent 38%),
             radial-gradient(circle at 10% 95%,#f0b3c4 0,transparent 30%),
             radial-gradient(circle at 95% 85%,#f2b9c9 0,transparent 32%),
             linear-gradient(#fdf4f7,#f9e3ea)}
.page{position:absolute;left:93px;top:18px;width:811px;height:1177px;background:rgba(255,255,255,.9);
  border-radius:8px;box-shadow:0 0 6px rgba(0,0,0,.25)}
.logo{left:107px;top:52px;display:flex;align-items:center;gap:8px}
.logo-dot{width:26px;height:26px;border-radius:50%;background:var(--purple)}
.logo-name{font-size:38px;font-weight:600;color:#4a4a4a;letter-spacing:-1px}
.phone{left:367px;top:60px;font-size:30px;font-weight:300;font-style:italic;color:#444}
.account{left:592px;top:64px;font-size:12px;color:var(--orange)}
.welcome{left:593px;top:81px;font-size:11px;color:#555}
.cart-bouquet{left:694px;top:30px;width:88px;height:88px;border-radius:50%;
  background:radial-gradient(circle,#b45c9c,#7d3a74 60%,#5f7a4a)}
.cart{left:779px;top:63px;width:115px;height:36px;border-radius:4px;
  background:linear-gradient(#f06464,#d22f2f);color:#fff;font-size:12px;font-weight:600;
  display:flex;align-items:center;justify-content:center;padding-left:14px;box-shadow:0 2px 2px rgba(0,0,0,.25)}
.nav{left:103px;top:140px;width:791px;height:40px;border-radius:6px;
  background:linear-gradient(#3a4652,var(--navy));box-shadow:0 3px 4px rgba(0,0,0,.3)}
.nav a{font-size:13px;font-weight:600;color:#c77bd4;text-decoration:none;position:absolute;top:12px}
.nav .active{left:0;top:0;width:124px;height:40px;border-radius:6px 0 0 6px;background:linear-gradient(#9d4cab,#6b2878);
  color:#fff;display:flex;align-items:center;padding-left:32px}
.search{position:absolute;left:662px;top:10px;width:119px;height:19px;border-radius:10px;background:#2b3640;
  border:1px solid #4d5a66;font-size:8px;color:#8995a0;padding:3px 12px}
.hero{left:103px;top:181px;width:791px;height:353px;
  background:linear-gradient(90deg,#f2e7da 0%,#e9d6bd 40%,#b98d62 70%,#6e4b30 100%)}
.hero-bouquet{left:500px;top:185px;width:280px;height:250px;border-radius:50%;
  background:radial-gradient(circle at 50% 40%,#e9c9d6,#8b5a7f 45%,#6e7d4a 70%,transparent 72%)}
.headline{left:115px;font-family:'Oswald',sans-serif;font-weight:300;color:var(--purple);font-size:34px;line-height:1;letter-spacing:-.5px}
.buy{left:125px;top:394px;width:106px;height:34px;border-radius:4px;background:linear-gradient(#9d4cab,#6b2878);
  color:#fff;font-size:15px;font-weight:700;display:flex;align-items:center;padding-left:9px;gap:8px;box-shadow:0 2px 3px rgba(0,0,0,.3)}
.badge{left:304px;top:330px;width:150px;height:150px;border-radius:50%;background:var(--red);
  border:5px solid #fff;box-shadow:0 0 0 1px #ccc;color:#fff;text-align:center;
  display:flex;flex-direction:column;align-items:center;justify-content:center}
.badge-top{font-size:9px;font-weight:700;line-height:12px;letter-spacing:.3px}
.badge-pct{font-size:34px;font-weight:700;line-height:40px}
.badge-foot{font-family:'Oswald',sans-serif;font-size:16px;line-height:20px}
.tile-frame{width:227px;height:150px;top:518px;border-radius:6px;background:rgba(255,255,255,.85);box-shadow:0 0 4px rgba(0,0,0,.2)}
.tile{top:528px;width:211px;height:140px;overflow:hidden;font-family:'Exo 2',sans-serif;font-style:italic;font-weight:800;color:#fff}
.sale{background:radial-gradient(circle at 70% 20%,#9a6ad0,#2d3c9c 50%,#132064)}
.hand{background:linear-gradient(90deg,#e53a4d,#f3a0a8 70%,#f4d3c6)}
.free{background:linear-gradient(#e24040,#c22828 50%,#2f9a3d 50%,#1f7e2c)}
.products{left:103px;top:691px;width:791px;height:302px;border-radius:6px;background:#fff;box-shadow:0 0 4px rgba(0,0,0,.2)}
.products-head{height:41px;border-radius:6px 6px 0 0;background:var(--lilac);color:#fff;font-size:25px;font-weight:600;padding:4px 17px}
.product{top:742px;width:180px}
.product-img{width:170px;height:121px}
.product h3{font-size:16px;font-weight:600;color:var(--orange);margin-top:12px}
.product p{font-size:9px;line-height:14px;color:#444;margin-top:2px}
.price{font-size:15px;font-weight:600;color:var(--purple);margin-top:2px}
.shop{position:absolute;right:10px;top:213px;width:63px;height:22px;border-radius:3px;background:linear-gradient(#9d4cab,#5e2068);
  color:#fff;font-size:10px;font-weight:700;display:flex;align-items:center;justify-content:center}
.sep{top:738px;width:0;height:245px;border-left:1px dotted var(--lilac)}
.footer{left:93px;top:1012px;width:811px;height:150px;background:var(--footer)}
.col{top:1024px}
.col h4{font-size:13px;font-weight:600;color:#4a4a4a;margin-bottom:6px}
.col li{list-style:none;font-size:10px;line-height:17px;color:#333}
.col li::before{content:"›";margin-right:5px;color:#555}
.contact p{font-size:10px;line-height:17px;color:#333}
.contact b{font-weight:700}
.card{width:43px;height:29px;border-radius:3px;display:flex;align-items:center;justify-content:center;
  font-size:7px;font-weight:700;color:#fff;box-shadow:0 1px 2px rgba(0,0,0,.3);text-align:center;line-height:1}
.copy{left:0;width:1000px;top:1173px;text-align:center;font-size:10px;color:#555}
.guild{left:850px;top:1166px;width:38px;height:24px;border-radius:4px;background:#e6a24a}
</style>
</head>
<body>
<div class="backdrop" role="img" aria-label="Soft pink roses filling the page background"></div>
<div class="page"></div>

<div class="abs logo"><span class="logo-dot"></span><span class="logo-name">Jo &amp; Mira's</span></div>
<div class="abs phone">0203 554 2071</div>
<div class="abs account">Your Account</div>
<div class="abs welcome">Welcome ( Log in )</div>
<div class="abs cart">Cart (empty)</div>
<div class="abs cart-bouquet" role="img" aria-label="Bouquet of purple roses"></div>

<nav class="abs nav">
  <a class="active" href="#">HOME</a>
  <a href="#" style="left:158px">ABOUT US</a>
  <a href="#" style="left:311px">WOLDWIDE DELIVERY</a>
  <a href="#" style="left:537px">CONTACT US</a>
  <div class="search">Search...</div>
</nav>

<div class="abs hero" role="img" aria-label="Hand-tied bouquet in hessian on a rustic wooden table"></div>
<div class="abs hero-bouquet" role="img" aria-label="Calla lilies and pink roses bouquet"></div>
<div class="abs headline" style="top:196px">HAND DELIVERED AND</div>
<div class="abs headline" style="top:244px">HAND PREPARED BY</div>
<div class="abs headline" style="top:288px;left:118px;font-weight:400;font-size:31px">A PROFESSIO NAL FLOIST</div>
<svg class="abs" style="left:110px;top:320px" width="16" height="60"><path d="M12 2 L4 30 L12 58" fill="none" stroke="#555" stroke-width="2"/></svg>
<svg class="abs" style="left:872px;top:320px" width="16" height="60"><path d="M4 2 L12 30 L4 58" fill="none" stroke="#555" stroke-width="2"/></svg>
<div class="abs buy">BYE NOW <svg width="9" height="12"><path d="M0 0 L9 6 L0 12Z" fill="#fff"/></svg></div>

<div class="abs badge">
  <div class="badge-top">7 DAYS OF<br>FLOWER FRESHNESS</div>
  <div class="badge-pct">100%</div>
  <div class="badge-foot">GUARANTEED</div>
</div>

<div class="abs tile-frame" style="left:120px"></div>
<div class="abs tile-frame" style="left:384px"></div>
<div class="abs tile-frame" style="left:651px"></div>
<div class="abs tile sale" style="left:129px" role="img" aria-label="Purple flower on deep blue, sale 20% off">
  <div class="abs" style="left:4px;top:108px;transform:rotate(-90deg);transform-origin:left top;font-family:Georgia,serif;font-style:normal;font-weight:400;font-size:34px">SALE</div>
  <div class="abs" style="left:50px;top:42px;font-family:'Open Sans',sans-serif;font-style:normal;font-weight:300;font-size:84px;line-height:1">20%</div>
</div>
<div class="abs tile hand" style="left:392px" role="img" aria-label="Red roses held by a smiling florist">
  <div class="abs" style="left:16px;top:0;font-size:40px;line-height:1.1">HAND</div>
  <div class="abs" style="left:11px;top:40px;font-size:34px;color:#9b3aa8">DELIVERY</div>
  <div class="abs" style="left:12px;top:94px;font-size:14px;line-height:20px">AND HAND PREPARED BY<br>A PROFESSIONAL FLORIST</div>
</div>
<div class="abs tile free" style="left:660px" role="img" aria-label="Red flowers behind a green delivery van">
  <div class="abs" style="left:14px;top:-6px;font-size:58px;color:#ffd7ef">FREE</div>
  <div class="abs" style="left:8px;top:74px;font-size:22px">DELIVERY WITH</div>
  <div class="abs" style="left:50px;top:104px;font-size:22px;color:#163d18">ALL ORDERS</div>
</div>

<section class="abs products"><div class="products-head">Featured products</div></section>
<svg class="abs" style="left:108px;top:827px" width="14" height="60"><path d="M11 2 L4 30 L11 58" fill="none" stroke="#b98ac3" stroke-width="2"/></svg>
<svg class="abs" style="left:874px;top:827px" width="14" height="60"><path d="M3 2 L10 30 L3 58" fill="none" stroke="#b98ac3" stroke-width="2"/></svg>

<div class="abs product" style="left:129px">
  <div class="product-img" role="img" aria-label="Bouquet of red roses, marked new" style="background:radial-gradient(circle,#e8432d,#b3231a 55%,#f4f1ee 80%)"></div>
  <h3>Roses are Red</h3>
  <p>It is a long established fact that a reader<br>wlong established<br>fact that act that a reader will</p>
  <div class="price">From £49.99</div><div class="shop">Shop Now!</div>
</div>
<div class="abs sep" style="left:309px"></div>
<div class="abs product" style="left:319px">
  <div class="product-img" role="img" aria-label="Bright mixed bouquet of pink and peach flowers" style="background:radial-gradient(circle,#f59aa6,#e2477b 55%,#6b5a4d)"></div>
  <h3>We are Young,</h3>
  <p>It is a long established fact that a reader<br>wlong established<br>fact that act that a reader will</p>
  <div class="price">From £19.99</div><div class="shop">Shop Now!</div>
</div>
<div class="abs sep" style="left:499px"></div>
<div class="abs product" style="left:509px">
  <div class="product-img" role="img" aria-label="Pale pink and white wedding flowers" style="background:radial-gradient(circle,#f7e0dc,#d9b9b6 50%,#5f7a5a)"></div>
  <h3>Wedding flower</h3>
  <p>It is a long established fact that a reader<br>wlong established<br>fact that act that a reader will</p>
  <div class="price">From £00.00</div><div class="shop">Shop Now!</div>
</div>
<div class="abs sep" style="left:688px"></div>
<div class="abs product" style="left:697px">
  <div class="product-img" role="img" aria-label="Lilac and green autumn arrangement in a rustic pot" style="background:radial-gradient(circle,#c6b2d6,#8a7aa0 45%,#4c5a44 75%,#3a3a38)"></div>
  <h3>Autumn Wonders</h3>
  <p>It is a long established fact that a reader<br>wlong established<br>fact that act that a reader will</p>
  <div class="price">From £27.99</div><div class="shop">Shop Now!</div>
</div>

<footer class="abs footer"></footer>
<div class="abs col" style="left:103px"><h4>Payment Vissuals</h4></div>
<div class="abs card" style="left:104px;top:1049px;background:#3d7d4a">Northern<br>Swift</div>
<div class="abs card" style="left:157px;top:1049px;background:#f2f2f2;color:#c33">Cardwell</div>
<div class="abs card" style="left:104px;top:1090px;background:#1f3f8c">PAYRO</div>
<div class="abs card" style="left:157px;top:1090px;background:#f2f2f2;color:#1f4f9c">Quikpay</div>

<div class="abs col" style="left:258px"><h4>Information</h4><ul><li>FAQ's</li><li>Corporate</li><li>Blog</li><li>New Cookie Policy</li></ul></div>
<div class="abs col" style="left:394px"><h4>Flower Delivery</h4><ul><li>Hints &amp; Tips</li><li>Terms &amp; Conditions</li><li>Privacy Policy</li></ul></div>
<div class="abs col" style="left:537px"><h4>jo&amp;mira's</h4><ul><li>Home</li><li>About Us</li><li>Wold Wide Delivery</li><li>Contact &nbsp;Us</li></ul></div>
<div class="abs col contact" style="left:662px"><h4>Contact Details</h4>
  <p><b>Central London:</b> 0203 554 2071</p>
  <p><b>Greater London:</b> 0208 417 2359 (Greater London)</p>
  <p><b>Marlow:</b> 01628 570213 (Marlow)</p>
  <p><b>Mobile:</b> 07845 190627</p>
  <p><b>Orders:</b> orders@joandmiras.co.uk</p>
  <p><b>Customer Service:</b> CS@joandmiras.co.uk</p>
</div>
<div class="abs copy">Copyrights © 2012-2013 jo&amp;mira's. All Rights Reserved</div>
<div class="abs guild" role="img" aria-label="The National Petal Guild member badge"></div>
</body>
</html>
```